Real Estate Investing company needs a business card design

We need a business card design for new Real Estate Investment Company called "Brightgate Holdings, LLC." We buy homes for cash and close quickly in any situation. Our company provides an easy and fast option for home owners who are in tough situations who need to sell their home fast and don't want realtor fees or other listing hassles. We also renovate and resell our homes which helps provide housing for the community. We would like to see designs that use the colors blue and white to match our company logo or other colors that may match our company logo. The final design should communicate trust and easy process.
Industry/Entity Type
Business
Contact Information for Business Card
Front should have company name and company logo. back of card should have company logo and area to list services.
Look and feel

```html
<!DOCTYPE html>
<html lang="en">
<head>
<meta charset="utf-8">
<title>Brightgate Holdings — Business Card</title>
<link rel="stylesheet" href="https://fonts.googleapis.com/css2?family=Open+Sans:wght@400;600;800&display=swap">
<style>
  :root {
    --brand-blue: #0b6fbf;
    --card-blue: #0a72c0;
    --ink: #1c1c1c;
    --panel-black: #1d1d1f;
    --paper: #ffffff;
    --backdrop: #e9ecef;
    --muted-white: #f2f2f2;
  }
  * { margin: 0; padding: 0; box-sizing: border-box; }
  html, body {
    width: 1200px; height: 900px; overflow: hidden;
    background: var(--backdrop);
    font-family: "Open Sans", Arial, sans-serif;
  }
  .canvas { position: relative; width: 1200px; height: 900px; }

  .card {
    position: absolute;
    overflow: hidden;
    box-shadow: 0 6px 18px rgba(0,0,0,0.18);
  }

  /* Front */
  .card-front {
    left: 237px; top: 60px; width: 556px; height: 344px;
    background: var(--paper);
  }
  .card-front .band { position: absolute; inset: 0; }
  .wordmark {
    position: absolute; left: 0; width: 100%; top: 48px;
    display: flex; justify-content: center; align-items: center; gap: 12px;
  }
  .wordmark-square {
    width: 22px; height: 22px; background: var(--brand-blue);
  }
  .wordmark-name {
    color: var(--brand-blue);
    font-weight: 800; font-size: 32px; letter-spacing: 0.5px;
    text-transform: uppercase; line-height: 1;
  }
  .person {
    position: absolute; left: 60px; width: 185px; top: 240px;
    text-align: right;
  }
  .person-name { color: var(--brand-blue); font-weight: 600; font-size: 18px; line-height: 24px; }
  .person-title { color: var(--muted-white); font-size: 15px; line-height: 20px; }
  .contact {
    position: absolute; left: 262px; top: 242px;
    color: var(--muted-white); font-size: 15px; line-height: 20px;
    list-style: none;
  }
  .contact li { display: flex; align-items: center; gap: 10px; }
  .contact svg { width: 12px; height: 12px; fill: var(--brand-blue); }
  .address {
    position: absolute; left: 106px; top: 300px;
    color: var(--muted-white); font-size: 15px;
  }

  /* Back */
  .card-back {
    left: 457px; top: 518px; width: 560px; height: 342px;
    background: var(--card-blue);
    color: var(--ink);
    text-align: center;
  }
  .back-name {
    margin-top: 50px;
    font-weight: 800; text-transform: uppercase; color: var(--ink);
    line-height: 1;
  }
  .back-name .line-one { display: block; font-size: 46px; letter-spacing: 1px; }
  .back-name .line-two { display: block; font-size: 34px; letter-spacing: 2px; margin-top: 6px; }
  .services { margin-top: 24px; padding: 0 40px; font-size: 15px; line-height: 20px; }
  .services p + p { margin-top: 18px; }
</style>
</head>
<body>
<main class="canvas">

  <section class="card card-front" aria-label="Business card front">
    <svg class="band" viewBox="0 0 556 344" aria-hidden="true">
      <rect x="0" y="196" width="556" height="148" fill="var(--panel-black)"/>
      <polygon points="0,151 498,151 498,131 558,174 490,217 490,202 0,202" fill="var(--paper)"/>
      <polygon points="0,154 501,154 501,137 553,174 493,211 493,198 0,198" fill="var(--brand-blue)"/>
    </svg>

    <div class="wordmark">
      <span class="wordmark-square"></span>
      <span class="wordmark-name">Brightgate Holdings</span>
    </div>

    <div class="person">
      <div class="person-name">Daniel Reyes</div>
      <div class="person-title">Managing Director</div>
    </div>

    <ul class="contact">
      <li>
        <svg viewBox="0 0 24 24"><path d="M6.6 10.8a15 15 0 0 0 6.6 6.6l2.2-2.2c.3-.3.7-.4 1-.2 1.1.4 2.3.6 3.6.6.6 0 1 .4 1 1V20c0 .6-.4 1-1 1A17 17 0 0 1 3 4c0-.6.4-1 1-1h3.5c.6 0 1 .4 1 1 0 1.3.2 2.5.6 3.6.1.3 0 .7-.2 1z"/></svg>
        <span>044-555 010 234</span>
      </li>
      <li>
        <svg viewBox="0 0 24 24"><path d="M2 5h20v14H2z M2 5l10 8 10-8" /></svg>
        <span>hello@brightgate.example</span>
      </li>
    </ul>

    <div class="address">210 Harbor Lane, Springfield, 45012</div>
  </section>

  <section class="card card-back" aria-label="Business card back">
    <h1 class="back-name">
      <span class="line-one">Brightgate</span>
      <span class="line-two">Holdings</span>
    </h1>
    <div class="services">
      <p>We buy homes for cash and close quickly in any situation.</p>
      <p>Our company provides an easy and fast option for home owners who are in tough situations who need to sell their home fast and don't want realtor fees or other listing hassles.</p>
      <p>We also renovate and resell our homes which helps provide housing for the community.</p>
    </div>
  </section>

</main>
</body>
</html>
```